We need a Welcome Booklet designed for our Church - Larkspur Commons Fellowship. We would like a design that is contemporary with no religious symbols or old pictures. Please use quality contemporary photos . See attached a Word document with what content we want in the booklet.

Target Market(s)

Guests to the church so new person friendly

Requirements
Must have
• A contemporary modern look
Should not have
• Religious symbols or old pictures

```html
<!DOCTYPE html>
<html lang="en">
<head>
<meta charset="utf-8">
<title>Larkspur Commons Fellowship – Welcome Booklet</title>
<link href="https://fonts.googleapis.com/css2?family=Bitter:wght@400&family=Mulish:wght@700;800&family=Questrial&display=swap" rel="stylesheet">
<style>
  :root {
    --ink: #1f1f1f;
    --white: #ffffff;
    --link-red: #e3221b;
    --circle-blue: #3a8ee6;
    --header-dark: #1d2a12;
    --header-green: #4f6e2a;
    --mark-navy: #151b26;
    --pantry-green: #6fb83a;
    --photo-warm: #b0482d;
    --photo-amber: #d78a55;
    --photo-room: #8f6a4e;
  }
  * { margin: 0; padding: 0; box-sizing: border-box; }
  html, body { width: 855px; height: 1200px; overflow: hidden; background: var(--white); }
  body { position: relative; font-family: "Questrial", sans-serif; color: var(--ink); }

  .page-header {
    position: absolute; left: 0; top: 0; width: 855px; height: 199px;
    background: linear-gradient(180deg, var(--header-green) 0%, #34491b 45%, var(--header-dark) 100%);
  }
  .page-header h1 {
    position: absolute; left: 61px; top: 118px;
    font-family: "Bitter", serif; font-weight: 400; font-size: 43px; color: var(--white);
  }

  .body-copy { position: absolute; font-size: 22px; line-height: 29px; }
  .intro { left: 56px; top: 219px; width: 725px; }
  .more-info { left: 56px; top: 418px; width: 560px; }
  .more-info a { font-family: "Mulish", sans-serif; color: var(--link-red); font-weight: 800; text-decoration: none; }
  .foodbank-text { left: 56px; top: 888px; width: 630px; line-height: 28px; }
  .stewards-text { left: 53px; top: 1026px; width: 625px; line-height: 28px; }
  .stewards-text strong { font-family: "Mulish", sans-serif; font-weight: 800; }

  .photo { position: absolute; }
  .photo-audience {
    left: 211px; top: 495px; width: 374px; height: 210px;
    background: radial-gradient(circle at 35% 55%, var(--photo-amber) 0%, var(--photo-warm) 45%, #5a2418 100%);
  }
  .photo-speaker {
    left: 567px; top: 618px; width: 237px; height: 174px;
    background: linear-gradient(180deg, #6b4d3a 0%, var(--photo-room) 55%, #4a3a30 100%);
  }

  .invite-circle {
    position: absolute; left: 42px; top: 484px; width: 236px; height: 236px;
    border-radius: 50%; background: var(--circle-blue); border: 9px solid var(--white);
    display: flex; align-items: center; justify-content: center; text-align: center;
    color: var(--white); font-family: "Mulish", sans-serif; font-weight: 800; font-size: 25px; line-height: 33px;
  }

  .partner-mark {
    position: absolute; display: flex; align-items: center; gap: 10px;
    font-family: "Mulish", sans-serif; font-weight: 800;
  }
  .partner-mark .shape { flex: none; }
  .event-mark { left: 604px; top: 515px; width: 204px; font-size: 24px; line-height: 29px; color: var(--mark-navy); }
  .event-mark .shape { width: 18px; height: 18px; background: var(--mark-navy); }
  .pantry-mark { left: 680px; top: 922px; width: 140px; font-size: 22px; line-height: 26px; color: var(--pantry-green); }
  .pantry-mark .shape { width: 16px; height: 16px; border-radius: 50%; background: var(--pantry-green); }
  .stewards-mark { left: 695px; top: 1048px; width: 130px; font-size: 21px; line-height: 25px; color: var(--ink); }
  .stewards-mark .shape { width: 16px; height: 16px; border-radius: 50%; background: var(--ink); }

  .section-title {
    position: absolute; left: 59px; top: 732px;
    font-family: "Bitter", serif; font-weight: 400; font-size: 47px; line-height: 46px;
  }
  .block-title {
    position: absolute; left: 60px; top: 848px;
    font-family: "Mulish", sans-serif; font-weight: 800; font-size: 22px;
  }
</style>
</head>
<body>
  <header class="page-header" role="img" aria-label="Photo of a seated conference audience with a green tint">
    <h1>First conference</h1>
  </header>

  <p class="body-copy intro">It is our culture here at LCF to begin a New Year by Putting God First. We dedicate the year by focusing on God, seeking Him for guidance, wisdom and direction for ourselves, family and for the church. Further, we go on a devotional journey for 21 days where take time to fast, pray, read God’s Word and listen to His direct for the upcoming year.</p>

  <p class="body-copy more-info">To know more about our First Conference please visit: <a href="#">larkspurcommons.org/firstconference</a></p>

  <div class="photo photo-audience" role="img" aria-label="Photo of a speaker facing a blurred conference audience"></div>
  <div class="photo photo-speaker" role="img" aria-label="Photo of a speaker at a lectern addressing a seated hall"></div>

  <div class="invite-circle">Come<br>and be a<br>part of<br>our first<br>conference</div>

  <div class="partner-mark event-mark"><span class="shape"></span>New Year Gathering</div>

  <h2 class="section-title">Community<br>and outreach</h2>

  <h3 class="block-title">Foodbank</h3>
  <p class="body-copy foodbank-text">We run a foodbank that provide short-term assistance to those in need of food. Our aim is to give those in need not just food, but hope; we always offer prayer at the Foodbank and seek to connect them to other services that can help improve their lives.</p>

  <div class="partner-mark pantry-mark"><span class="shape"></span>Larkspur Pantry</div>

  <p class="body-copy stewards-text"><strong>Night Stewards</strong> is a project involving volunteers from local churches working together to ensure everyone who visits the city on a Friday or Saturday night encounters a safe, vibrant environment.</p>

  <div class="partner-mark stewards-mark"><span class="shape"></span>Night Stewards</div>
</body>
</html>
```